Communication and Marketing agency needs a new presentation card

We are a group of communication and marketing agencies specialized in companies that are in the logistics and industrial sector. The head agency is VELUNEX Grupo and the group consists of 4 agencies: VELUNEX Media, VELUNEX Digital, VELUNEX Research and PlanoDeImagenes. We hace 4 offices in Spain (Madrid, Barcelona, Valencia and Murcia). We are looking for a clean and attractive design that transmits our experience, brand presence in the market and knowledge to those who receive the card.It has to maintain the colors of the logo that is attached.
logistics and industrial sector
Marketing department
Clean and attractive design

```html
<!DOCTYPE html>
<html lang="en">
<head>
<meta charset="utf-8">
<title>VELUNEX Grupo – Business Card</title>
<link href="https://fonts.googleapis.com/css2?family=Bebas+Neue&family=PT+Sans:ital,wght@0,400;0,700;1,700&display=swap" rel="stylesheet">
<style>
  :root {
    --backdrop: #a09f9e;
    --paper: #fbfbfb;
    --brand-red: #b0222a;
    --ink: #2f2f2f;
    --ink-soft: #3a3a3a;
  }
  html, body {
    margin: 0;
    width: 1200px;
    height: 1200px;
    overflow: hidden;
    background: var(--backdrop);
  }
  .card {
    position: absolute;
    left: 223px;
    width: 815px;
    height: 465px;
    background: var(--paper);
    font-family: "PT Sans", sans-serif;
    color: var(--ink);
  }
  .card--front { top: 76px; }
  .card--back { top: 658px; }

  .wordmark {
    position: absolute;
    text-align: right;
    font-family: "Bebas Neue", sans-serif;
    color: var(--brand-red);
    line-height: 1;
  }
  .wordmark__name { display: block; font-size: 98px; letter-spacing: 4px; }
  .wordmark__sub { display: block; font-size: 72px; margin-top: 4px; letter-spacing: 1px; }
  .card--front .wordmark { right: 86px; top: 36px; }
  .card--back .wordmark { right: 185px; top: 154px; }

  .person { position: absolute; left: 68px; top: 250px; }
  .person__name {
    font-family: "Bebas Neue", sans-serif;
    font-size: 46px;
    line-height: 1;
    margin: 0;
    color: var(--ink);
    letter-spacing: 0.5px;
  }
  .person__name .first { color: var(--brand-red); }
  .person__role { font-size: 18px; margin-top: 8px; color: var(--ink-soft); }

  .rule {
    position: absolute;
    top: 336px;
    width: 51px;
    height: 3px;
    background: var(--brand-red);
  }
  .rule--left { left: 68px; }
  .rule--right { left: 554px; }

  .contact-list {
    position: absolute;
    top: 350px;
    font-size: 18px;
    line-height: 23.5px;
    margin: 0;
    padding: 0;
    list-style: none;
  }
  .contact-list--left { left: 68px; }
  .contact-list--right { left: 554px; top: 346px; }
  .contact-list .label { color: var(--brand-red); font-weight: 700; }
  .contact-list .accent { color: var(--brand-red); }

  .site-link {
    position: absolute;
    left: 0;
    right: 0;
    top: 408px;
    text-align: center;
    font-size: 21px;
    font-style: italic;
    font-weight: 700;
    color: var(--ink-soft);
  }
  .site-link .chevrons { color: var(--brand-red); margin: 0 10px; }
</style>
</head>
<body>

<section class="card card--front">
  <div class="wordmark">
    <span class="wordmark__name">VELUNEX</span>
    <span class="wordmark__sub">Grupo</span>
  </div>

  <div class="person">
    <h1 class="person__name"><span class="first">Marco</span> Ledesma</h1>
    <div class="person__role">MANAGER</div>
  </div>

  <div class="rule rule--left"></div>
  <ul class="contact-list contact-list--left">
    <li><span class="label">P.</span> +(34) -915- 4472</li>
    <li><span class="label">F.</span> +(34) -915- 4473</li>
    <li>marco@velunexgrupo.es</li>
  </ul>

  <div class="rule rule--right"></div>
  <ul class="contact-list contact-list--right">
    <li>Calle Serrano 48,</li>
    <li>28001 Madrid, España</li>
    <li>www.<span class="accent">velunexgrupo</span>.com</li>
  </ul>
</section>

<section class="card card--back">
  <div class="wordmark">
    <span class="wordmark__name">VELUNEX</span>
    <span class="wordmark__sub">Grupo</span>
  </div>
  <div class="site-link"><span class="chevrons">&gt;&gt;</span>www.velunex.com<span class="chevrons">&lt;&lt;</span></div>
</section>

</body>
</html>
```